A brochure website design
Product: Mivra coconut yogurt
Specialty of the product:
Mivra coconut yogurt is a non dairy yogurt using coconut cream powder and coconut water as its major ingredients. It contains live cultures and is a great alternatives to dairy yogurt.
It is gluten free, soy free, preservative free, lactose free, non-GMO and no artificial sweetener. It is a great choice for paleo diet.
4. About Mivra
Mivra is developed by a group of coconut lovers who believe that promoting vegan based diet can contribute to the wellness of the world and the sustainability of living. Our vision is to end cruelty to animal and minimise the world’s reliance on milk farming. We believe that cow milk is belonged to cow BB and God has already provided coconut to us which is actually more suitable to human’s body than dairy product.
5. Our products
Mivra coconut yogurt 120g
Mivra coconut yogurt with raspberry 150g
6. Mivra recipes
7. About coconut
8. Contact us
9. Stores finder
Target Market(s)
Age 18 to 50 . People looking for life style and healthy diet.
Industry/Entity Type
Product
Number of Pages Required
5+ page
Look and feel
Each slider illustrates characteristics of the customer's brand and the style your logo design should communicate.

```html
<!DOCTYPE html>
<html lang="en">
<head>
<meta charset="utf-8">
<title>Mivra Yoghurt</title>
<link href="https://fonts.googleapis.com/css2?family=Open+Sans:ital,wght@0,300;0,400;0,600;0,700;0,800;1,400&display=swap" rel="stylesheet">
<style>
:root{
  --teal:#4aa1b6;
  --teal-dark:#3f8ea2;
  --green:#6dbb67;
  --green-dark:#5aa955;
  --ink:#333;
  --text:#666;
  --muted:#999;
  --soft:#f7f7f7;
  --line:#ddd;
  --white:#fff;
}
*{margin:0;padding:0;box-sizing:border-box}
html,body{width:679px;height:1200px;overflow:hidden}
body{position:relative;background:var(--white);font-family:"Open Sans",sans-serif;color:var(--text)}
.abs{position:absolute}
a{color:inherit;text-decoration:none}

/* top bar */
.topbar{left:0;top:0;width:679px;height:15px;background:var(--teal);color:var(--white);font-size:5.6px;letter-spacing:.2px}
.topbar span{position:absolute;top:4px;display:flex;align-items:center;gap:3px}
.topbar i{display:inline-block;width:5px;height:5px;border-radius:1px;background:var(--white);opacity:.9}

/* header */
.header{left:0;top:15px;width:679px;height:53px;background:var(--white)}
.logo{left:74px;top:17px;font-size:14px;font-weight:700;color:var(--teal);letter-spacing:.2px}
.nav{left:221px;top:18px;display:flex;gap:0;font-size:5.8px;color:var(--ink);align-items:center}
.nav a{padding:0 10px;line-height:17px}
.nav a.active{background:var(--green);color:var(--white);border-radius:2px;padding:0 8px}
.search{left:595px;top:37px}

/* hero */
.hero{left:0;top:68px;width:679px;height:280px;background:var(--soft)}
.hero-title{left:74px;top:127px;font-size:25px;color:var(--teal);font-weight:300;letter-spacing:.5px;line-height:1}
.hero-title b{font-weight:800}
.hero-sub{left:74px;top:163px;font-size:6.4px;color:var(--green);letter-spacing:.2px}
.hero-copy{left:74px;top:180px;font-size:6.8px;line-height:15px;color:var(--text)}
.btn-green{left:74px;top:218px;width:107px;height:21px;background:var(--green);color:var(--white);font-size:5.8px;font-weight:700;display:flex;align-items:center;justify-content:center;border-radius:2px}
.dots{left:74px;top:267px;display:flex;gap:3px}
.dots span{width:13px;height:13px;border-radius:50%;background:#ccc}
.product-art{left:336px;top:112px;width:268px;height:180px;border-radius:10px;background:linear-gradient(180deg,#f4f8f9 0%,#4aa1b6 45%,#4db861 90%)}

/* welcome */
.section-title{left:0;width:679px;text-align:center;font-size:16px;font-weight:300;color:var(--ink);letter-spacing:.3px}
.section-title b{font-weight:700}
.welcome-copy{left:100px;top:397px;width:478px;text-align:center;font-size:6.2px;line-height:13.6px;color:var(--text)}
.card{top:462px;width:152px;height:134px;background:var(--white);border:1px solid var(--line);text-align:center}
.card::before,.card::after{content:"";position:absolute;inset:-1px;border:1px solid #e6e6e6;z-index:-1}
.card::before{transform:rotate(2.5deg)}
.card::after{transform:rotate(-1.5deg)}
.card svg{margin-top:12px}
.card h3{margin-top:4px;font-size:7.4px;font-weight:400;color:var(--teal)}
.card p{margin-top:3px;font-size:5.4px;line-height:12px;color:var(--text)}
.btn-teal{display:inline-block;margin-top:7px;width:47px;height:17px;line-height:17px;background:var(--teal);color:var(--white);font-size:5.6px;border-radius:2px}

/* products */
.products{left:0;top:642px;width:679px;height:215px;background:var(--green)}
.products .section-title{color:var(--white);top:34px}
.pack{width:100px;height:100px;border-radius:50%;background:var(--white);border:3px solid var(--green-dark);display:flex;align-items:center;justify-content:center}
.pack div{width:70px;height:64px;border-radius:6px;background:linear-gradient(180deg,#eef5f7 0%,#4aa1b6 40%,#4db861 90%)}
.prod{color:var(--white);width:130px}
.prod h4{font-size:7.2px;font-weight:700;letter-spacing:.3px;line-height:16px}
.prod p{font-size:5.8px;line-height:13px;margin-top:1px}
.prod a{display:block;margin:12px 0 0 6px;font-size:5.2px;font-weight:700;letter-spacing:.3px}

/* reviews */
.arrows{left:592px;top:894px;font-size:8px;color:var(--muted);letter-spacing:3px}
.avatar{left:76px;top:918px;width:60px;height:60px;border-radius:50%;background:radial-gradient(circle at 50% 40%,#a0705a 0%,#5a3e30 60%,#2d4a36 100%)}
.quote{left:168px;top:929px;width:436px;font-size:6.9px;line-height:15px;font-style:italic;color:var(--text)}
.quote .mark{font-size:14px;color:#ccc;font-style:normal;vertical-align:-3px;margin-right:2px}
.quote-name{left:168px;top:963px;font-size:5.4px;font-weight:700;color:var(--green);letter-spacing:.3px}
.quote-end{left:562px;top:947px;font-size:14px;color:#ddd}

/* footer */
.footer{left:0;top:1018px;width:679px;height:142px;background:var(--soft)}
.foot-head{top:1041px;font-size:7.2px;color:var(--ink);letter-spacing:.2px}
.foot-head::after{content:"";display:block;margin-top:3px;width:27px;height:1.5px;background:var(--teal)}
.foot-list{font-size:6px;line-height:13.6px;color:var(--text)}
.contact-row{display:flex;gap:7px;font-size:5.8px;line-height:13.6px;color:var(--text);align-items:flex-start}
.contact-row i{flex:none;width:11px;height:11px;border-radius:50%;background:var(--teal);display:flex;align-items:center;justify-content:center;margin-top:1px}
.input{left:389px;top:1068px;width:113px;height:18px;background:var(--white);border:1px solid #e3e3e3;font-size:4.6px;color:#aaa;padding:6px 6px}
.subscribe{left:389px;top:1094px;width:51px;height:16px;background:var(--teal);color:var(--white);font-size:5px;font-weight:700;display:flex;align-items:center;justify-content:center;border-radius:2px}
.social{display:flex;align-items:center;gap:6px;font-size:6px;color:var(--text);height:18px}
.social i{width:16px;height:16px;border-radius:50%;background:var(--teal)}
.bottombar{left:0;top:1160px;width:679px;height:40px;background:var(--white);text-align:center;font-size:6px;color:var(--ink);padding-top:15px}
</style>
</head>
<body>

<div class="abs topbar">
  <span style="left:74px"><i></i>: 555-014-2230</span>
  <span style="left:140px"><i></i>: 555-014-2231</span>
  <span style="left:366px"><i></i>LOGIN</span>
  <span style="left:413px"><i></i>REGISTER</span>
  <span style="left:466px"><i></i>REQUEST QUOTE</span>
  <span style="left:538px"><i></i>SEND US FEEDBACK</span>
</div>

<header class="abs header"></header>
<div class="abs logo">MIVRAYOGHURT</div>
<nav class="abs nav" style="top:33px">
  <a class="active">HOME</a><a>ABOUT</a><a>PRODUCTS</a><a>MIVRA RECIPES</a><a>ABOUT COCONUT</a><a>CONTACT US</a><a>STORE FINDER</a>
</nav>
<svg class="abs search" width="10" height="10" viewBox="0 0 10 10" style="top:37px">
  <circle cx="4.2" cy="4.2" r="3.3" fill="none" stroke="var(--green)" stroke-width="1"/>
  <line x1="6.6" y1="6.6" x2="9.2" y2="9.2" stroke="var(--green)" stroke-width="1"/>
</svg>

<section class="abs hero"></section>
<h1 class="abs hero-title">COCONUT <b>YOGURT</b></h1>
<div class="abs hero-sub">VOLUPTATEM QUIA VOLUPTAS SIT ASPERNATUR AUT...</div>
<p class="abs hero-copy">Aspernatur aut odit aut fugit, sed quia consequuntur dolores<br>eos qui ratione voluptatem sequi nesciunt...</p>
<a class="abs btn-green">VIEW MORE INFORMATION</a>
<div class="abs dots"><span></span><span></span></div>
<div class="abs product-art" role="img" aria-label="Two Mivra coconut yogurt cups, large and small, in teal and green packaging with coconut halves"></div>

<svg class="abs" style="left:0;top:296px" width="679" height="56" viewBox="0 0 679 56" aria-hidden="true">
  <path d="M0 34 C120 20 200 8 330 20 C450 32 520 60 679 12 L679 56 L0 56 Z" fill="var(--white)"/>
  <path d="M112 20 C230 10 330 14 420 32 C500 48 590 46 679 10 L679 18 C590 56 500 54 420 40 C330 22 230 16 112 20 Z" fill="var(--green)"/>
</svg>

<h2 class="abs section-title" style="top:368px">WELCOME <b>MIVRAYOGHURT</b></h2>
<p class="abs welcome-copy">Mivra is developed by a group of coconut lovers who believe that promoting vegan based diet can contribute to the wellness of the world and the sustainability of living. Our vision is to end cruelty to animal and minimise the world's reliance on milk farming. We believe that cow milk is belonged to cow BB and God has already provided coconut to us which is actually more suitable to human's body than dairy product.</p>

<article class="abs card" style="left:80px">
  <svg width="36" height="38" viewBox="0 0 36 38" fill="none" stroke="var(--teal)" stroke-width="1.3">
    <path d="M18 12 C17 20 16 28 15 33"/><path d="M18 12 C12 6 6 8 4 13"/><path d="M18 12 C24 5 31 7 33 12"/><path d="M18 12 C14 4 18 1 22 2"/><path d="M18 12 C22 14 25 19 24 23"/><path d="M4 36 C10 30 26 30 32 36 Z"/>
  </svg>
  <h3>Nemo enim ipsam</h3>
  <p>Nemo enim ipsam voluptatem quia voluptas<br>consequuntur magni dolores...</p>
  <a class="btn-teal">VIEW MORE</a>
</article>
<article class="abs card" style="left:264px">
  <svg width="36" height="38" viewBox="0 0 36 38" fill="none" stroke="var(--teal)" stroke-width="1.3">
    <circle cx="18" cy="21" r="15"/><ellipse cx="18" cy="14" rx="9" ry="4"/><path d="M20 13 L27 2 L31 3"/><path d="M10 28 C14 32 22 32 26 28"/>
  </svg>
  <h3>Nemo enim ipsam</h3>
  <p>Nemo enim ipsam voluptatem quia voluptas<br>consequuntur magni dolores...</p>
  <a class="btn-teal">VIEW MORE</a>
</article>
<article class="abs card" style="left:448px">
  <svg width="38" height="38" viewBox="0 0 38 38" fill="none" stroke="var(--teal)" stroke-width="1.3">
    <circle cx="19" cy="11" r="6"/><circle cx="9" cy="15" r="5"/><circle cx="29" cy="15" r="5"/><path d="M9 34 C9 24 29 24 29 34 Z"/><path d="M2 30 C2 23 8 21 11 22"/><path d="M36 30 C36 23 30 21 27 22"/>
  </svg>
  <h3>Nemo enim ipsam</h3>
  <p>Nemo enim ipsam voluptatem quia voluptas<br>consequuntur magni dolores...</p>
  <a class="btn-teal">VIEW MORE</a>
</article>

<section class="abs products">
  <h2 class="abs section-title">OUR <b>PRODUCTS</b></h2>
</section>
<div class="abs pack" style="left:76px;top:716px"><div role="img" aria-label="Mivra coconut yogurt 120g cup"></div></div>
<div class="abs prod" style="left:194px;top:722px">
  <h4>MIVRA COCONUT YOGURT 120G</h4>
  <p>Nemo enim ipsam voluptatem quia voluptas<br>sit aspernatur aut odit aut fugit, sed quia<br>consequuntur magni dolores eos...</p>
  <a>VIEW MORE INFO</a>
</div>
<div class="abs pack" style="left:364px;top:716px"><div role="img" aria-label="Mivra coconut yogurt with raspberry 150g cup"></div></div>
<div class="abs prod" style="left:482px;top:722px;width:140px">
  <h4>MIVRA COCONUT YOGURT WITH<br>RASPBERRY 150G</h4>
  <p>Nemo enim ipsam voluptatem quia voluptas<br>consequuntur magni dolores eos...</p>
  <a>VIEW MORE INFO</a>
</div>

<h2 class="abs section-title" style="top:890px">CUSTOMER <b>REVIEW'S</b></h2>
<div class="abs arrows">‹ ›</div>
<div class="abs avatar" role="img" aria-label="Customer portrait photo"></div>
<p class="abs quote"><span class="mark">“</span>Lorem Ipsum is simply dummy text of the printing and typesetting industry. Lorem Ipsum has been the industry's standard dummy text ever since the 1500s, when an unknown printer took a galley of type and scrambled it to make a type specimen book...</p>
<div class="abs quote-end">”</div>
<div class="abs quote-name">-MARCUS ELDEN</div>

<footer class="abs footer"></footer>
<h4 class="abs foot-head" style="left:74px">NAVIGATION</h4>
<div class="abs foot-list" style="left:74px;top:1066px">Home<br>About<br>Products<br>Mivra Recipes</div>
<div class="abs foot-list" style="left:126px;top:1066px">About Coconut<br>Contact us<br>Store finder</div>

<h4 class="abs foot-head" style="left:222px">CONTACT INFO</h4>
<div class="abs contact-row" style="left:222px;top:1066px"><i><svg width="5" height="6" viewBox="0 0 5 6"><path d="M2.5 6 L0.4 2.6 A2.2 2.2 0 1 1 4.6 2.6 Z" fill="var(--white)"/></svg></i><span>18 Palm Grove Lane, Coral Street,<br>Seaview-2210</span></div>
<div class="abs contact-row" style="left:222px;top:1097px"><i><svg width="6" height="6" viewBox="0 0 6 6"><path d="M1 0.5 L2.3 0.5 L2.8 2 L2 2.6 Q2.8 4 4 4.2 L4.6 3.4 L6 3.9 L6 5.2 Q3 6 0.6 2.6 Q0.3 1.2 1 0.5Z" fill="var(--white)"/></svg></i><span>Phone : (555) 019-4420</span></div>
<div class="abs contact-row" style="left:222px;top:1116px"><i><svg width="6" height="5" viewBox="0 0 6 5"><rect x="0.4" y="0.4" width="5.2" height="4.2" fill="none" stroke="var(--white)" stroke-width=".8"/><path d="M0.4 0.6 L3 2.8 L5.6 0.6" fill="none" stroke="var(--white)" stroke-width=".8"/></svg></i><span>Email : hello@mivrayoghurt.example</span></div>

<h4 class="abs foot-head" style="left:389px">NEWSLETTER</h4>
<div class="abs input">ENTER EMAIL ADDRESS</div>
<a class="abs subscribe">SUBSCRIBE</a>

<h4 class="abs foot-head" style="left:550px">FOLLOW US</h4>
<div class="abs social" style="left:550px;top:1067px"><i></i>Social Feed</div>
<div class="abs social" style="left:550px;top:1085px"><i></i>Short Posts</div>
<div class="abs social" style="left:550px;top:1103px"><i></i>Circles</div>

<div class="abs bottombar">Copyrights © mivrayoghurt.2016 | Allrights Reserved.</div>

</body>
</html>
```